RT Pemberly Electric Yard Sign

Looking to have a yard sign designed that we can place at projects we are working on. Most likely will be 18" H x 24" W but flexible that we can increase the size if necessary. It should include our logo, our phone # 609-555-0147, website rtpemberlyelectric-example.com and slogan, built on integrity, driven by excellence. Colors should match our brand.

```html
<!DOCTYPE html>
<html lang="en">
<head>
<meta charset="utf-8">
<title>RT Pemberly Electric Yard Sign</title>
<link href="https://fonts.googleapis.com/css2?family=Saira+Semi+Condensed:wght@400;700;800&display=swap" rel="stylesheet">
<style>
  :root {
    --navy: #0f2a5e;
    --red: #e3231b;
    --peach: #f4a07c;
    --white: #ffffff;
    --backdrop: #e9edf2;
  }
  html, body {
    margin: 0;
    padding: 0;
    width: 1200px;
    height: 1200px;
    overflow: hidden;
    background: var(--backdrop);
  }
  .sign {
    position: absolute;
    left: 40px;
    top: 180px;
    width: 1120px;
    height: 840px;
    background: var(--white);
    font-family: "Saira Semi Condensed", sans-serif;
    color: var(--navy);
  }
  .sign-frame {
    position: absolute;
    inset: 0;
  }
  .brand {
    position: absolute;
    top: 62px;
    left: 0;
    width: 100%;
    display: flex;
    justify-content: center;
    align-items: center;
    gap: 22px;
  }
  .brand-mark {
    width: 40px;
    height: 40px;
    background: var(--red);
  }
  .brand-name {
    font-size: 64px;
    font-weight: 700;
    letter-spacing: 1px;
    color: var(--navy);
    line-height: 1;
  }
  .quote-mark {
    position: absolute;
    left: 0;
    width: 100%;
    text-align: center;
    font-size: 190px;
    font-weight: 800;
    color: var(--peach);
    line-height: 1;
  }
  .quote-open { top: 196px; }
  .quote-close { top: 512px; }
  .slogan {
    position: absolute;
    top: 300px;
    left: 0;
    width: 100%;
    margin: 0;
    text-align: center;
    line-height: 1.06;
    font-size: 104px;
  }
  .slogan-strong { font-weight: 700; display: block; }
  .slogan-light { font-weight: 400; display: block; }
  .phone {
    position: absolute;
    top: 612px;
    left: 0;
    width: 100%;
    text-align: center;
    font-size: 140px;
    font-weight: 800;
    color: var(--red);
    line-height: 1;
  }
  .website-row {
    position: absolute;
    top: 774px;
    left: 35px;
    width: 1050px;
    height: 44px;
    display: flex;
    align-items: center;
  }
  .website-rule {
    flex: 1;
    height: 4px;
    background: var(--navy);
  }
  .website {
    padding: 0 20px;
    font-size: 42px;
    font-weight: 400;
    color: var(--navy);
    line-height: 1;
    letter-spacing: 1px;
    white-space: nowrap;
  }
</style>
</head>
<body>
  <div class="sign">
    <svg class="sign-frame" width="1120" height="840" viewBox="0 0 1120 840" aria-hidden="true">
      <g fill="none" stroke="var(--navy)" stroke-width="4">
        <polyline points="82,108 35,108 35,798"/>
        <polyline points="1038,108 1085,108 1085,798"/>
      </g>
      <g stroke="var(--red)" stroke-width="5">
        <line x1="180" y1="265" x2="493" y2="265"/>
        <line x1="627" y1="265" x2="905" y2="265"/>
        <line x1="135" y1="553" x2="497" y2="553"/>
        <line x1="620" y1="553" x2="982" y2="553"/>
      </g>
      <line x1="330" y1="170" x2="990" y2="170" stroke="var(--red)" stroke-width="5"/>
    </svg>

    <div class="brand">
      <span class="brand-mark"></span>
      <span class="brand-name">RT Pemberly Electric</span>
    </div>

    <div class="quote-mark quote-open">&ldquo;</div>

    <p class="slogan">
      <span class="slogan-strong">Built On Integrity,</span>
      <span class="slogan-light">Driven By Excellence</span>
    </p>

    <div class="quote-mark quote-close">&rdquo;</div>

    <div class="phone">609-555-0147</div>

    <div class="website-row">
      <span class="website-rule"></span>
      <span class="website">rtpemberlyelectric-example.com</span>
      <span class="website-rule"></span>
    </div>
  </div>
</body>
</html>
```